AUSTRALIAN CONSULTING FIRM BUSINESS CARD - MODERN

We are wanting a modern, clean lined business card design. We are professional niche consultancy firm situated in Australia called Harbrook Advisory Partners Pty Ltd.
The card should communicate professionalism and creativity and draw on our logo design (attached).
The design should be two sided, landscape orientation.
Target Market(s)
government, not for profit sector, corporate clients
Industry/Entity Type
Landscape
Requirements
Must have
- logo
no new introduced colours

```html
<!DOCTYPE html>
<html lang="en">
<head>
<meta charset="utf-8">
<title>Harbrook Advisory Partners – Business Card</title>
<link rel="stylesheet" href="https://fonts.googleapis.com/css2?family=Roboto:wght@400;500;700;900&display=swap">
<style>
  :root {
    --stage: #e6e7eb;
    --card-white: #ffffff;
    --brand-blue: #2b49a6;
    --brand-navy: #1f3a93;
    --brand-purple: #8a3a9b;
    --brand-magenta: #c0509e;
    --text-dark: #3a3a3a;
    --text-light: #ffffff;
  }
  * { box-sizing: border-box; margin: 0; padding: 0; }
  html, body {
    width: 1200px;
    height: 900px;
    overflow: hidden;
    background: var(--stage);
    font-family: "Roboto", Arial, sans-serif;
  }
  .canvas {
    position: relative;
    width: 1200px;
    height: 900px;
    display: flex;
    flex-direction: column;
    align-items: center;
    justify-content: center;
    gap: 40px;
  }
  .card {
    position: relative;
    width: 700px;
    height: 400px;
    border-radius: 4px;
    box-shadow: 0 6px 18px rgba(0, 0, 0, 0.15);
    overflow: hidden;
  }

  /* Back side */
  .card-back {
    background: linear-gradient(135deg, #2f52b3 0%, var(--brand-blue) 55%, #243f95 100%);
  }
  .card-back .wordmark {
    position: absolute;
    right: 48px;
    bottom: 52px;
    text-align: right;
    color: var(--text-light);
    font-weight: 700;
    line-height: 1.1;
  }
  .card-back .wordmark-main { display: block; font-size: 58px; letter-spacing: -0.5px; }
  .card-back .wordmark-sub { display: block; font-size: 17px; letter-spacing: 0.5px; text-transform: uppercase; }

  /* Front side */
  .card-front { background: var(--card-white); }
  .card-front .brand {
    position: absolute;
    left: 56px;
    top: 48px;
    display: flex;
    align-items: center;
    gap: 12px;
  }
  .card-front .brand-dot {
    width: 18px;
    height: 18px;
    border-radius: 50%;
    background: var(--brand-purple);
  }
  .card-front .brand-name {
    color: var(--brand-navy);
    font-weight: 700;
    font-size: 26px;
    letter-spacing: -0.2px;
  }
  .contact-list {
    position: absolute;
    left: 56px;
    top: 118px;
    list-style: none;
  }
  .contact-item {
    display: flex;
    align-items: center;
    gap: 10px;
    height: 26px;
    font-size: 15px;
    color: var(--text-dark);
  }
  .contact-icon {
    width: 18px;
    height: 18px;
    flex: none;
  }
  .divider {
    position: absolute;
    left: 56px;
    right: 56px;
    top: 262px;
    height: 1px;
    background: var(--brand-purple);
  }
  .person {
    position: absolute;
    right: 56px;
    top: 232px;
    text-align: right;
  }
  .person-name {
    font-size: 18px;
    font-weight: 500;
    letter-spacing: 1px;
    text-transform: uppercase;
    color: var(--text-dark);
  }
  .person-title {
    margin-top: 14px;
    font-size: 15px;
    color: var(--brand-purple);
  }
</style>
</head>
<body>
<main class="canvas">

  <section class="card card-back" aria-label="Business card back">
    <div class="wordmark">
      <span class="wordmark-main">Harbrook</span>
      <span class="wordmark-sub">Advisory Partners Pty Ltd</span>
    </div>
  </section>

  <section class="card card-front" aria-label="Business card front">
    <div class="brand">
      <span class="brand-dot"></span>
      <span class="brand-name">Harbrook Advisory Partners Pty Ltd</span>
    </div>

    <ul class="contact-list">
      <li class="contact-item">
        <svg class="contact-icon" viewBox="0 0 18 18" aria-hidden="true">
          <rect width="18" height="18" rx="2" fill="var(--brand-purple)"/>
          <path d="M9 3.5a3.5 3.5 0 0 0-3.5 3.5c0 2.6 3.5 7 3.5 7s3.5-4.4 3.5-7A3.5 3.5 0 0 0 9 3.5zm0 4.8a1.3 1.3 0 1 1 0-2.6 1.3 1.3 0 0 1 0 2.6z" fill="#fff"/>
        </svg>
        48 Coastline Road Suite 2, Avoca NSW 2251
      </li>
      <li class="contact-item">
        <svg class="contact-icon" viewBox="0 0 18 18" aria-hidden="true">
          <rect width="18" height="18" rx="2" fill="var(--brand-purple)"/>
          <path d="M6 4l2 2.5-1.2 1.3c.7 1.4 1.9 2.6 3.3 3.3L11.5 10 14 12l-1 2c-4.5-.3-8.3-4.1-8.6-8.6z" fill="#fff"/>
        </svg>
        0243 555 019
      </li>
      <li class="contact-item">
        <svg class="contact-icon" viewBox="0 0 18 18" aria-hidden="true">
          <rect width="18" height="18" rx="2" fill="var(--brand-purple)"/>
          <rect x="4" y="5.5" width="10" height="7" rx="1" fill="none" stroke="#fff" stroke-width="1.3"/>
          <path d="M4.5 6l4.5 3.5L13.5 6" fill="none" stroke="#fff" stroke-width="1.3"/>
        </svg>
        info@harbrookadvisory.com
      </li>
      <li class="contact-item">
        <svg class="contact-icon" viewBox="0 0 18 18" aria-hidden="true">
          <rect width="18" height="18" rx="2" fill="var(--brand-purple)"/>
          <circle cx="9" cy="9" r="4.8" fill="none" stroke="#fff" stroke-width="1.2"/>
          <ellipse cx="9" cy="9" rx="2" ry="4.8" fill="none" stroke="#fff" stroke-width="1"/>
          <path d="M4.2 9h9.6" stroke="#fff" stroke-width="1"/>
        </svg>
        www.harbrookadvisory.com
      </li>
    </ul>

    <div class="divider"></div>

    <div class="person">
      <p class="person-name">Daniel Marsh</p>
      <p class="person-title">President</p>
    </div>
  </section>

</main>
</body>
</html>
```